" Trata-se de uma construtora em conjunto com um escritório de engenharia e arquitetura para prestar serviços de construção, gerenciamento de obras e projetos e desenho. "

```html
<!DOCTYPE html>
<html lang="pt-BR">
<head>
<meta charset="UTF-8">
<title>Alvenor — Construção, Engenharia e Arquitetura</title>
<link rel="stylesheet" href="https://fonts.googleapis.com/css2?family=Poppins:wght@300;400;500;600;700&display=swap">
<style>
  :root {
    --header-bg: #2b2b2b;
    --brand-box: #3a3a3a;
    --accent: #e0962a;
    --white: #ffffff;
    --hero-light: #e9ecef;
    --hero-mid: #c9cfd4;
    --hero-warm: #d8c65a;
    --text-shadow: rgba(0, 0, 0, 0.35);
  }
  * { margin: 0; padding: 0; box-sizing: border-box; }
  html, body {
    width: 1200px;
    height: 1200px;
    overflow: hidden;
    background: var(--header-bg);
    font-family: "Poppins", sans-serif;
  }
  .page {
    position: relative;
    width: 1200px;
    height: 1200px;
  }
  .site-header {
    position: absolute;
    top: 0; left: 0;
    width: 1200px;
    height: 200px;
    background: var(--header-bg);
    z-index: 2;
  }
  .brand {
    position: absolute;
    top: 0;
    left: 120px;
    width: 280px;
    height: 300px;
    background: var(--brand-box);
    display: flex;
    align-items: center;
    justify-content: center;
    gap: 14px;
  }
  .brand-mark {
    width: 18px;
    height: 18px;
    background: var(--accent);
  }
  .brand-name {
    color: var(--white);
    font-weight: 600;
    font-size: 44px;
    letter-spacing: 0;
  }
  .main-nav {
    position: absolute;
    top: 0;
    right: 120px;
    height: 200px;
    display: flex;
    align-items: center;
    gap: 64px;
  }
  .main-nav a {
    color: var(--white);
    text-decoration: none;
    font-weight: 600;
    font-size: 26px;
  }
  .hero {
    position: absolute;
    top: 200px; left: 0;
    width: 1200px;
    height: 1000px;
    overflow: hidden;
  }
  .hero-photo {
    position: absolute;
    inset: 0;
    background:
      linear-gradient(180deg, rgba(0,0,0,0.05) 0%, rgba(0,0,0,0.25) 100%),
      linear-gradient(170deg, var(--hero-light) 0%, var(--hero-mid) 45%, var(--hero-warm) 58%, var(--hero-light) 70%, var(--hero-mid) 100%);
  }
  .hero-content {
    position: absolute;
    top: 300px;
    left: 0;
    width: 1200px;
    text-align: center;
    color: var(--white);
    text-shadow: 0 2px 10px var(--text-shadow);
  }
  .hero-title {
    margin: 0 auto;
    width: 1100px;
    font-weight: 700;
    font-size: 64px;
    letter-spacing: -1.5px;
    line-height: 1.12;
  }
  .hero-subtitle {
    margin: 40px auto 0;
    width: 1000px;
    font-weight: 300;
    font-size: 36px;
    line-height: 1.4;
  }
  .hero-cta {
    display: inline-block;
    margin-top: 70px;
    padding: 30px 56px;
    background: var(--accent);
    color: var(--white);
    font-weight: 600;
    font-size: 26px;
    text-decoration: none;
    text-shadow: none;
  }
  .slider-dots {
    position: absolute;
    bottom: 56px;
    left: 0;
    width: 1200px;
    display: flex;
    justify-content: center;
    gap: 22px;
  }
  .slider-dot {
    width: 20px;
    height: 20px;
    border-radius: 50%;
    border: 3px solid var(--white);
  }
  .slider-dot.is-active { background: var(--white); }
</style>
</head>
<body>
<div class="page">
  <header class="site-header">
    <div class="brand">
      <span class="brand-mark"></span>
      <span class="brand-name">Alvenor</span>
    </div>
    <nav class="main-nav">
      <a href="#">Home</a>
      <a href="#">Quem Somos</a>
    </nav>
  </header>

  <section class="hero">
    <div class="hero-photo" role="img" aria-label="Fotografia de plantas arquitetônicas sobre a mesa com régua amarela, lápis e óculos, e um profissional ao fundo"></div>
    <div class="hero-content">
      <h1 class="hero-title">Mude sua forma de relacionar com sua obra</h1>
      <p class="hero-subtitle">Estabelecemos vínculos reais e humanos com clientes, oferecendo serviços transparentes, de qualidade e no prazo.</p>
      <a class="hero-cta" href="#">Conheça-nos</a>
    </div>
    <div class="slider-dots">
      <span class="slider-dot is-active"></span>
      <span class="slider-dot"></span>
      <span class="slider-dot"></span>
    </div>
  </section>
</div>
</body>
</html>
```